I-71 Website for Washington D.C Cannabis Business

We need a website with a 21+ age (yes/no/captcha) verification
5 Pages listed on a top banner
Home/Splash Page-Should send back to splash & ask for 21+ veri
Shop-
about Us
Blog
Contact us:

Content for pages:
Splash Page - Contains How it works with 1-6 steps
1. Register for Rewards Or Head to {Link} for more anonymous Use
2. Choose Cookies & Free Gifts
3. Submit Address & Order
4.Recieve Confirmation Text
5.Send Separate Selfie and Clear Drivers License Picture
6.Enjoy Your Cookies and Free Gifts

Shop/Menu Page - Empty with top banner (will fill in this section)

Home- Should link back to Splash page
About Us-
"Welcome to Maple Parcel, Where Everyday is a Maple Day! We believe that everyone who chooses to enjoy the medicinal and relaxing benefits cannabis, should have safe and reliable access. And no matter your lifestyle or level of wellness, you deserve access to friendly customer service and professional courtesy. At Maple Parcel we provide Artisan Cookies that come with I-71 Gifted premium exotic cannabis + edibles & accessories. We provide an excellent variety of cookies and gifts, and all purchases improve your community!

For every 5 Cookies you purchase we donate 50 Sandwiches to Local DC Organizations that help our community members in need. In this way, you’ll be supporting the local DC community by purchasing from Maple Parcel (We also have Sandwich Rewards!!)

Maple Parcel is and always will be committed to providing DC The Best Service, Gifts & Experience. Always. We are committed to setting a standard for the gifting business in DC.

We appreciate you taking the time to check us out! We are here for all of your I-71 compliant needs.

Need to reach us? Please send all business related inquiries/compliments/complaints to Mapleparceldc@velnormail.com and we will reach out ASAP. We look forward to hearing from you!

-MP

Blog- This should be Fillable
Contact US: Should be fillable with text or graphic

Similar Websites to check out: https://www.dcqenlowfarm.com/
https://www.amberloftvista.com/

Target Market(s)

DC/Cannabis market

Coding

Coded - Design and coding required

Number of Pages Required

5+ page

Font styles to use
Other font styles liked:
• Sans Serif

Colors
0455a3
33b8a4
ffffff

Requirements
Must have
• 21+ age (yes/no/captcha) verification
I-71 Compliant
Color match the green to the logo
Nice to have
• I would like the website to have a fresh and fun look....without being corny
Cookie buttons (menu etc that look like a cookie)
Should not have
• No pictures of Marihuana

```html
<!DOCTYPE html>
<html lang="en">
<head>
<meta charset="utf-8">
<title>Maple Parcel — Website Screens</title>
<link rel="stylesheet" href="https://fonts.googleapis.com/css2?family=Roboto:wght@400;500;700;900&display=swap">
<style>
:root{
  --teal:#33b8a4;
  --teal-dark:#1f8f7e;
  --brand-blue:#0455a3;
  --ice:#eaf6fc;
  --paper:#f7f8f9;
  --ink:#111111;
  --body-ink:#444a4f;
  --backdrop:#f2f2f2;
  --white:#ffffff;
}
*{box-sizing:border-box;margin:0;padding:0}
html,body{width:1200px;height:2485px;overflow:hidden;background:var(--backdrop)}
body{font-family:'Roboto',sans-serif;color:var(--ink)}
.stage{position:relative;width:1244px;height:2576px;transform:scale(0.96463);transform-origin:0 0}
.screen{position:absolute;left:77px;width:1090px;background:var(--ice);box-shadow:0 18px 40px rgba(0,0,0,.12);overflow:hidden}
.screen--gate{top:64px;height:794px}
.screen--splash{top:922px;height:794px}
.screen--about{top:1780px;height:732px;background:var(--paper)}

.brand-head{position:absolute;left:0;top:0;width:100%;height:105px;display:flex;align-items:center;justify-content:center;gap:10px}
.brand-dot{width:26px;height:26px;border-radius:50%;background:var(--teal)}
.brand-name{font-weight:700;font-size:24px;color:var(--brand-blue);letter-spacing:.5px}

.rules-bar{position:absolute;left:0;top:105px;width:100%;height:40px;background:var(--teal);display:flex;align-items:center;justify-content:center;gap:34px;color:var(--white);font-size:16px;font-weight:500}
.rule{display:flex;align-items:center;gap:8px}
.tick{width:28px;height:28px;border-radius:50%;background:var(--teal-dark);display:flex;align-items:center;justify-content:center}

.hero{position:absolute;left:0;top:145px;width:100%;height:590px;background:
  radial-gradient(ellipse 300px 200px at 20% 25%,#c79a66 0%,transparent 70%),
  radial-gradient(ellipse 360px 240px at 75% 55%,#b98552 0%,transparent 70%),
  radial-gradient(ellipse 260px 180px at 55% 8%,#a8784a 0%,transparent 70%),
  linear-gradient(160deg,#8a6a4c 0%,#6f5642 45%,#3d3632 80%,#2e2b2a 100%)}
.hero-shade{position:absolute;inset:0;background:rgba(40,30,22,.28)}
.hero-title{position:absolute;top:113px;width:100%;text-align:center;color:var(--white);font-size:40px;font-weight:700;letter-spacing:.5px}
.step{position:absolute;top:200px;width:130px;margin-left:-65px;text-align:center;color:var(--white)}
.step-art{width:58px;height:62px;margin:0 auto 12px;border-radius:10px;background:linear-gradient(160deg,#4fd0bb,#2a9c8b)}
.step-no{font-size:17px;font-weight:700;letter-spacing:.3px}
.step-text{font-size:12px;line-height:18px;margin-top:4px}
.shop-btn{position:absolute;left:443px;top:378px;width:205px;height:49px;background:var(--teal);color:var(--white);font-size:14px;font-weight:500;display:flex;align-items:center;justify-content:center;letter-spacing:.3px}

.site-foot{position:absolute;left:0;bottom:0;width:100%;height:59px;background:var(--ice)}
.socials{position:absolute;left:92px;top:11px;display:flex;gap:10px}
.social{width:38px;height:38px;border-radius:50%;background:var(--teal)}
.copyright{position:absolute;right:92px;top:20px;font-size:14px;color:var(--ink)}

.dim{position:absolute;inset:0;background:rgba(45,45,45,.55)}
.age-gate{position:absolute;left:236px;top:181px;width:618px;height:431px;background:var(--ice);text-align:center}
.gate-brand{margin-top:70px;display:flex;align-items:center;justify-content:center;gap:14px}
.gate-brand .brand-dot{width:44px;height:44px}
.gate-brand .brand-name{font-size:40px}
.gate-title{margin-top:64px;font-size:28px;font-weight:700;line-height:35px;text-transform:uppercase}
.gate-note{margin-top:10px;font-size:16px}
.gate-actions{margin-top:18px;display:flex;justify-content:center;gap:15px}
.gate-btn{width:102px;height:44px;font-size:17px;font-weight:500;display:flex;align-items:center;justify-content:center}
.gate-btn--yes{background:var(--teal);color:var(--white)}
.gate-btn--no{border:2px solid var(--teal);color:var(--teal)}

.top-nav{position:absolute;left:0;top:0;width:100%;height:93px;background:var(--ice)}
.nav-brand{position:absolute;left:92px;top:34px;display:flex;align-items:center;gap:8px}
.nav-brand .brand-dot{width:22px;height:22px}
.nav-brand .brand-name{font-size:20px}
.nav-links{position:absolute;left:320px;top:35px;display:flex;gap:42px;font-size:19px;font-weight:500}
.nav-call{position:absolute;left:813px;top:27px;display:flex;align-items:center;gap:10px}
.call-icon{width:38px;height:38px;border-radius:50%;background:var(--teal);display:flex;align-items:center;justify-content:center}
.call-label{font-size:16px;line-height:20px}
.call-number{font-size:19px;font-weight:500;line-height:22px}

.about{position:absolute;left:92px;top:132px;width:910px}
.about h1{font-size:36px;font-weight:900;margin-bottom:18px}
.about p{font-size:13px;line-height:21.5px;color:var(--body-ink);margin-bottom:21.5px}
.notice-band{position:absolute;left:0;top:579px;width:100%;height:73px;background:var(--teal);color:var(--white);font-size:15px;font-weight:500;line-height:22px;display:flex;flex-direction:column;align-items:center;justify-content:center}
.screen--about .site-foot{height:80px}
.screen--about .socials{top:24px}
.screen--about .copyright{top:33px}
</style>
</head>
<body>
<div class="stage">

  <!-- Age verification screen -->
  <section class="screen screen--gate">
    <header class="brand-head"><span class="brand-dot"></span><span class="brand-name">Maple Parcel</span></header>
    <div class="rules-bar">
      <span class="rule"><span class="tick"><svg width="14" height="14" viewBox="0 0 14 14"><path d="M2 7.5l3 3 7-7" fill="none" stroke="#fff" stroke-width="2"/></svg></span>Be 21+</span>
      <span class="rule"><span class="tick"><svg width="14" height="14" viewBox="0 0 14 14"><path d="M2 7.5l3 3 7-7" fill="none" stroke="#fff" stroke-width="2"/></svg></span>Have a Valid ID</span>
      <span class="rule"><span class="tick"><svg width="14" height="14" viewBox="0 0 14 14"><path d="M2 7.5l3 3 7-7" fill="none" stroke="#fff" stroke-width="2"/></svg></span>Have a Valid Delivery Address</span>
    </div>
    <div class="hero" role="img" aria-label="Close-up photo of chocolate chip cookies on baking paper">
      <div class="hero-shade"></div>
      <div class="step" style="left:149px"><div class="step-art" role="img" aria-label="Illustration of hands holding a phone"></div><div class="step-no">STEP 1</div><div class="step-text">Register for Rewards</div></div>
      <div class="step" style="left:946px"><div class="step-art" role="img" aria-label="Illustration of a hand holding a gift box"></div><div class="step-no">STEP 6</div><div class="step-text">Enjoy Your Cookies and Free Gifts</div></div>
    </div>
    <footer class="site-foot">
      <div class="socials"><span class="social" aria-label="Social link"></span><span class="social" aria-label="Social link"></span><span class="social" aria-label="Social link"></span></div>
      <div class="copyright">Copyright © All rights reserved. | Sitemap</div>
    </footer>
    <div class="dim"></div>
    <div class="age-gate">
      <div class="gate-brand"><span class="brand-dot"></span><span class="brand-name">Maple Parcel</span></div>
      <h2 class="gate-title">Please verify your age before<br>shopping our products!</h2>
      <p class="gate-note">You must be 21 years old to enter</p>
      <div class="gate-actions"><span class="gate-btn gate-btn--yes">Yes</span><span class="gate-btn gate-btn--no">No</span></div>
    </div>
  </section>

  <!-- Splash / how it works -->
  <section class="screen screen--splash">
    <header class="brand-head"><span class="brand-dot"></span><span class="brand-name">Maple Parcel</span></header>
    <div class="rules-bar">
      <span class="rule"><span class="tick"><svg width="14" height="14" viewBox="0 0 14 14"><path d="M2 7.5l3 3 7-7" fill="none" stroke="#fff" stroke-width="2"/></svg></span>Be 21+</span>
      <span class="rule"><span class="tick"><svg width="14" height="14" viewBox="0 0 14 14"><path d="M2 7.5l3 3 7-7" fill="none" stroke="#fff" stroke-width="2"/></svg></span>Have a Valid ID</span>
      <span class="rule"><span class="tick"><svg width="14" height="14" viewBox="0 0 14 14"><path d="M2 7.5l3 3 7-7" fill="none" stroke="#fff" stroke-width="2"/></svg></span>Have a Valid Delivery Address</span>
    </div>
    <div class="hero" role="img" aria-label="Close-up photo of chocolate chip cookies on baking paper">
      <div class="hero-shade"></div>
      <h2 class="hero-title">HOW IT WORKS</h2>
      <div class="step" style="left:149px"><div class="step-art" role="img" aria-label="Illustration of hands holding a phone"></div><div class="step-no">STEP 1</div><div class="step-text">Register for Rewards</div></div>
      <div class="step" style="left:324px"><div class="step-art" role="img" aria-label="Illustration of a finger tapping"></div><div class="step-no">STEP 2</div><div class="step-text">Choose Cookies &amp; Free Gifts</div></div>
      <div class="step" style="left:480px"><div class="step-art" role="img" aria-label="Illustration of a map with a pin"></div><div class="step-no">STEP 3</div><div class="step-text">Submit Address &amp; Order</div></div>
      <div class="step" style="left:635px"><div class="step-art" role="img" aria-label="Illustration of a confirmed envelope"></div><div class="step-no">STEP 4</div><div class="step-text">Recieve Confirmation Text</div></div>
      <div class="step" style="left:791px"><div class="step-art" role="img" aria-label="Illustration of stacked photos"></div><div class="step-no">STEP 5</div><div class="step-text">Send Separate Selfie and Clear Drivers License Picture</div></div>
      <div class="step" style="left:946px"><div class="step-art" role="img" aria-label="Illustration of a hand holding a gift box"></div><div class="step-no">STEP 6</div><div class="step-text">Enjoy Your Cookies and Free Gifts</div></div>
      <span class="shop-btn">CONTINUE TO SHOP »</span>
    </div>
    <footer class="site-foot">
      <div class="socials"><span class="social" aria-label="Social link"></span><span class="social" aria-label="Social link"></span><span class="social" aria-label="Social link"></span></div>
      <div class="copyright">Copyright © All rights reserved. | Sitemap</div>
    </footer>
  </section>

  <!-- About us page -->
  <section class="screen screen--about">
    <nav class="top-nav">
      <div class="nav-brand"><span class="brand-dot"></span><span class="brand-name">Maple Parcel</span></div>
      <div class="nav-links"><span>Home</span><span>Shop</span><span>About Us</span><span>Blog</span><span>Contact Us</span></div>
      <div class="nav-call">
        <span class="call-icon"><svg width="18" height="18" viewBox="0 0 24 24"><path d="M6.6 10.8a15 15 0 0 0 6.6 6.6l2.2-2.2a1 1 0 0 1 1-.25 11.4 11.4 0 0 0 3.6.6 1 1 0 0 1 1 1V20a1 1 0 0 1-1 1A17 17 0 0 1 3 4a1 1 0 0 1 1-1h3.5a1 1 0 0 1 1 1c0 1.25.2 2.45.6 3.6a1 1 0 0 1-.25 1z" fill="#fff"/></svg></span>
        <div><div class="call-label">Text or call:</div><div class="call-number">202 - 555 - 0147</div></div>
      </div>
    </nav>
    <article class="about">
      <h1>ABOUT US</h1>
      <p>Welcome to Maple Parcel, where everyday is a maple day! We believe that everyone who chooses to enjoy the medicinal and relaxing benefits cannabis, should have safe and reliable access. And no matter your lifestyle or level of wellness, you deserve access to friendly customer service and professional courtesy.&nbsp; At Maple Parcel we provide Artisan Cookies that come with I-71&nbsp; Gifted premium exotic cannabis + edibles &amp; accessories. We provide an excellent variety of cookies and gifts, and all purchases improve your community!</p>
      <p>For every 5 Cookies you purchase we donate 50 Sandwiches to Local DC Organizations that help our community members in need. In this way, you’ll be supporting the local DC community by purchasing from Maple Parcel (We also have Sandwich Rewards!!)</p>
      <p>Maple Parcel is and always will be committed to providing DC The Best Service, Gifts &amp; Experience. Always. We are committed to setting a standard for the gifting business in DC.</p>
      <p>We appreciate you taking the time to check us out! We are here for all of your I-71 compliant needs.</p>
      <p>Need to reach us? Please send all business related inquiries/compliments/complaints to Mapleparceldc@velnormail.com and we will reach out ASAP. We look forward to hearing from you!</p>
      <p>-MP</p>
    </article>
    <div class="notice-band"><span>Please call us to request service.</span><span>Initiative 71 compliant. Nothing is for sale on this website.</span></div>
    <footer class="site-foot">
      <div class="socials"><span class="social" aria-label="Social link"></span><span class="social" aria-label="Social link"></span><span class="social" aria-label="Social link"></span></div>
      <div class="copyright">Copyright © All rights reserved. | Sitemap</div>
    </footer>
  </section>

</div>
</body>
</html>
```